Business Card for Hollin Ledger - A cannabis publication for executives.

I'd like some business cards for Hollin Ledger. The logo is done (great job!) and I need a card design I will use with PELT. I made it a short project to allow time for printing before an event. These will be standard sized cards (final artwork size 3.66" x 2.16" at 300dpi) with a final card size of 3.5" x 2.0". (See PELT.example if you need more info.) I might try rounded corners but am not sure yet. I think the design will work okay with rounded.

Hollin Ledger will be a bi-weekly publication for the cannabis industry. It is targeted to investors and industry executives, not consumers or pot smokers. So our market is more B2B. However I am open to creativity and making the card something people remark on.

My contact for card:

Dara Venholm
Founder/CEO
dara@hollinledger.example

2746 Marrow Lane
Boston MA 02391
(617)555-0193

Target Market(s)

Executives, Industry people and investors in the Cannabis sector.

Contact Information for Business Card

PELT does do double sided and the second side can be the same or different images. Only one side is required but use of the second side would be a bonus.

Font styles to use
Serif
Sans Serif
Decorative

Colors

Designer to choose colors to be used in the design.

Requirements
Must have
• Logo, contact info
Nice to have
• Style and design to make the card stand out in a crowd.

```html
<!DOCTYPE html>
<html lang="en">
<head>
<meta charset="utf-8">
<title>Hollin Ledger — Business Card</title>
<link href="https://fonts.googleapis.com/css2?family=Montserrat:wght@500;600;700&display=swap" rel="stylesheet">
<style>
  :root {
    --backdrop: #d9dadb;
    --card: #fbfbfb;
    --ink: #1d1d1d;
    --brand-blue: #1777c4;
    --brand-green: #74ad2f;
  }
  * { box-sizing: border-box; margin: 0; padding: 0; }
  html, body {
    width: 1200px; height: 1200px; overflow: hidden;
    background: var(--backdrop);
    font-family: "Montserrat", Arial, sans-serif;
    color: var(--ink);
  }
  .sheet {
    width: 1200px; height: 1200px;
    display: flex; flex-direction: column; align-items: center; justify-content: center;
    gap: 52px;
  }
  .card {
    position: relative;
    width: 900px; height: 514px;
    background: var(--card);
    box-shadow: 0 10px 28px rgba(0,0,0,0.18);
    overflow: hidden;
  }
  .card__accents {
    position: absolute; inset: 0; width: 100%; height: 100%;
  }
  .accent--blue { fill: var(--brand-blue); }
  .accent--green { fill: var(--brand-green); }

  /* Logo side */
  .card--logo { display: flex; align-items: center; justify-content: center; }
  .wordmark {
    position: relative;
    display: flex; align-items: center; gap: 22px;
  }
  .wordmark__mark {
    width: 58px; height: 58px; border-radius: 50%;
    background: var(--brand-green);
  }
  .wordmark__name {
    font-weight: 600; font-size: 68px; letter-spacing: 0.5px;
    color: var(--brand-blue);
  }

  /* Contact side */
  .card--contact { display: flex; justify-content: center; }
  .contact {
    position: relative;
    margin-top: 108px;
    display: flex; flex-direction: column; align-items: center;
    text-align: center;
  }
  .contact__name { font-weight: 600; font-size: 54px; line-height: 1; }
  .contact__role { font-weight: 700; font-size: 24px; margin-top: 14px; }
  .contact__list { list-style: none; margin-top: 30px; }
  .contact__row {
    display: flex; align-items: flex-start; gap: 14px;
    font-weight: 600; font-size: 22px; line-height: 1.3;
    margin-bottom: 12px; text-align: left;
  }
  .contact__icon {
    flex: none; width: 38px; height: 38px; margin-top: -5px;
  }
  .contact__icon circle, .contact__icon path, .contact__icon rect {
    fill: none; stroke: var(--ink); stroke-width: 1.6;
  }
</style>
</head>
<body>
<main class="sheet">

  <section class="card card--logo" aria-label="Business card, logo side">
    <svg class="card__accents" viewBox="0 0 900 514" preserveAspectRatio="none" aria-hidden="true">
      <polygon class="accent--blue" points="0,120 16,120 16,268 0,288"/>
      <polygon class="accent--green" points="900,262 884,282 884,470 900,470"/>
    </svg>
    <div class="wordmark">
      <span class="wordmark__mark" aria-hidden="true"></span>
      <span class="wordmark__name">Hollin Ledger</span>
    </div>
  </section>

  <section class="card card--contact" aria-label="Business card, contact side">
    <svg class="card__accents" viewBox="0 0 900 514" preserveAspectRatio="none" aria-hidden="true">
      <polygon class="accent--blue" points="0,90 16,90 16,250 0,270"/>
      <polygon class="accent--green" points="900,250 884,270 884,470 900,470"/>
    </svg>
    <div class="contact">
      <h1 class="contact__name">Dara Venholm</h1>
      <p class="contact__role">Founder/CEO</p>
      <ul class="contact__list">
        <li class="contact__row">
          <svg class="contact__icon" viewBox="0 0 38 38" aria-hidden="true">
            <circle cx="19" cy="19" r="17"/>
            <rect x="10" y="13" width="18" height="12"/>
            <path d="M10 13 L19 20 L28 13"/>
          </svg>
          <span>dara@hollinledger.example</span>
        </li>
        <li class="contact__row">
          <svg class="contact__icon" viewBox="0 0 38 38" aria-hidden="true">
            <circle cx="19" cy="19" r="17"/>
            <path d="M19 27 C14 21 13 18 13 16 A6 6 0 0 1 25 16 C25 18 24 21 19 27 Z"/>
            <circle cx="19" cy="16" r="2.2"/>
          </svg>
          <span>2746 Marrow Lane<br>Boston MA 02391<br>(617)555-0193</span>
        </li>
      </ul>
    </div>
  </section>

</main>
</body>
</html>
```